Corvanti, LLC Website

Creating website for medical billing company.

Target Market(s)

Medical providers

Industry/Entity Type

Medical billing

Coding

Coded - Design and coding required

Number of Pages Required

3 page

Font styles to use
Other font styles liked:
• Fonts that match our logo.

Requirements
Must have
• First page (greeting and explanation of who we are). Second page something about me and company (I'll supply some content, make generic for now). And page three, information that people can give for us to contact them.
Nice to have
• A little animation. But not over-the-top. Colors that match our logo.
Should not have
• Over-the-top animation.

```html
<!DOCTYPE html>
<html lang="en">
<head>
<meta charset="utf-8">
<title>Corvanti, LLC – Website Design</title>
<link href="https://fonts.googleapis.com/css2?family=Mulish:wght@300;400;500;600;700&display=swap" rel="stylesheet">
<style>
:root{
  --navy-deep:#0e284b;
  --navy:#1c3764;
  --teal:#00b4cb;
  --mist:#f4f5f6;
  --board:#e3e7ec;
  --ink:#1c3764;
  --muted:#5d6878;
  --white:#ffffff;
}
*{margin:0;padding:0;box-sizing:border-box}
html,body{width:1200px;height:4174px;overflow:hidden}
body{background:var(--board);font-family:'Mulish',sans-serif;color:var(--ink);position:relative}
.abs{position:absolute}
.brand-board .wordmark{left:196px;top:166px;font-size:25px;font-weight:600;color:var(--navy)}
.brand-board .wordmark::before{content:"";position:absolute;left:48px;top:-44px;width:36px;height:36px;border-radius:50%;background:var(--teal)}
.board-label{font-size:22px;font-weight:400;color:var(--navy)}
.font-name{font-size:19px;color:#7c8592;font-weight:300}
.swatch{width:40px;height:40px;border-radius:50%}
.hex{font-size:9px;color:#6c7684;width:60px;text-align:center}

.site{position:absolute;left:222px;top:277px;width:792px;height:3792px;background:var(--white);overflow:hidden}
.site > *{position:absolute}

.hero{left:0;top:0;width:792px;height:441px;background:var(--navy);border-bottom-left-radius:66px;overflow:hidden}
.hero-photo{left:418px;top:0;width:374px;height:441px;background:linear-gradient(160deg,#1c3764 0%,#13305a 45%,#0a8ea6 80%,#00b4cb 100%)}
.nav{left:0;top:0;width:792px;height:42px;border-bottom:1px solid rgba(255,255,255,.12)}
.nav-brand{position:absolute;left:74px;top:14px;font-size:12px;font-weight:600;color:#fff;padding-left:18px}
.nav-brand::before{content:"";position:absolute;left:0;top:1px;width:13px;height:13px;border-radius:50%;background:var(--teal)}
.nav-links{position:absolute;left:300px;top:16px;display:flex;gap:22px;font-size:8px;color:#d6deea}
.nav-cta{position:absolute;left:627px;top:8px;width:91px;height:26px;border-radius:13px;background:var(--teal);color:#fff;font-size:8px;font-weight:700;text-align:center;line-height:26px}
.eyebrow{font-size:7px;letter-spacing:4px;color:var(--teal);text-transform:uppercase;font-weight:600}
.hero-title{left:74px;top:182px;font-size:44px;line-height:40px;font-weight:600;color:#fff}
.hero-sub{left:74px;top:290px;font-size:8.5px;line-height:13px;color:#dbe3ee;width:300px}
.btn-outline{left:74px;top:337px;width:91px;height:26px;border:1px solid var(--teal);border-radius:13px;color:#fff;font-size:7.5px;font-weight:700;text-align:center;line-height:24px}
.stat-badge{left:478px;top:235px;width:87px;height:100px;background:#fff;border-radius:8px;box-shadow:0 6px 18px rgba(0,0,0,.18);text-align:center}
.stat-badge p{font-size:6.5px;line-height:9px;color:var(--muted);margin-top:6px}

.perks{left:0;top:441px;width:792px;height:141px;background:var(--mist)}
.perk{position:absolute;top:54px;display:flex;align-items:center;gap:10px;font-size:9px;line-height:11px;color:var(--ink)}
.perk svg{flex:none}

.intro-mark{left:74px;top:640px;width:282px;height:282px;border-radius:50%;background:#e7f6f9}
.intro-mark span{position:absolute;left:0;top:124px;width:282px;text-align:center;font-size:30px;font-weight:600;color:var(--navy)}
.intro-text{left:454px;top:708px;width:262px}
.section-title{font-size:22px;font-weight:600;color:var(--navy)}
.body-copy{font-size:8.5px;line-height:13px;color:var(--muted)}

.services{left:0;top:978px;width:792px;height:441px;background:var(--mist);border-top-left-radius:66px}
.center{width:792px;text-align:center;left:0}
.card{position:absolute;top:127px;width:193px;height:219px;background:#fff;border-radius:6px;text-align:center;padding:40px 20px 0}
.card .icon{width:36px;height:36px;border-radius:50%;background:var(--mist);margin:0 auto 18px;display:flex;align-items:center;justify-content:center}
.card h3{font-size:9.5px;font-weight:500;color:var(--teal);margin-bottom:10px}
.card p{font-size:7.5px;line-height:11.5px;color:var(--muted)}

.proof{left:0;top:1419px;width:792px;height:159px;background:var(--navy-deep);border-bottom-right-radius:66px}
.proof-text{position:absolute;left:74px;top:56px;font-size:22px;line-height:26px;font-weight:500;color:#fff}
.proof-text em{font-style:normal;color:var(--teal)}
.proof-stat{position:absolute;top:58px;text-align:center;color:var(--teal);font-size:22px;font-weight:500}
.proof-stat small{display:block;font-size:7px;color:#c8d2e0;margin-top:2px}

.photo{border-radius:14px}
.row-title{font-size:21px;line-height:28px;font-weight:500;color:var(--navy)}
.checks{display:grid;grid-template-columns:120px 120px;row-gap:12px;font-size:7.5px;color:var(--muted)}
.checks span{display:flex;align-items:center;gap:6px}
.tick{width:9px;height:9px;border-radius:50%;background:var(--teal);display:inline-block;position:relative}
.tick::after{content:"";position:absolute;left:3px;top:1.5px;width:2px;height:4px;border:solid #fff;border-width:0 1.2px 1.2px 0;transform:rotate(45deg)}

.testimonial{left:0;top:2466px;width:792px;height:233px;background:var(--mist);border-top-left-radius:66px}

.contact-photo{left:0;top:2699px;width:395px;height:421px;background:linear-gradient(135deg,#2c6f9e 0%,#6c8aa6 45%,#c6cdd6 100%)}
.contact{left:395px;top:2699px;width:397px;height:421px;background:var(--navy)}
.field-label{font-size:6.5px;color:#c8d2e0}
.field{border:1px solid rgba(255,255,255,.35);border-radius:4px}
.btn-solid{background:var(--teal);color:#fff;border-radius:14px;font-size:7.5px;font-weight:700;text-align:center;line-height:28px}

.faq{left:0;top:3120px;width:792px;height:324px;background:var(--mist);border-top-right-radius:66px}
.faq-list{position:absolute;left:206px;top:123px;width:382px}
.faq-item{display:flex;justify-content:space-between;font-size:8px;color:var(--ink);height:35px;border-bottom:1px solid #dfe3e8;padding-top:3px}
.faq-item b{font-weight:400;color:var(--teal);font-size:10px}

.footer-brand{left:74px;top:3509px;font-size:13px;font-weight:600;color:var(--navy);padding-left:20px}
.footer-brand::before{content:"";position:absolute;left:0;top:1px;width:14px;height:14px;border-radius:50%;background:var(--teal)}
.socials{left:676px;top:3512px;display:flex;gap:6px}
.socials i{width:9px;height:9px;border-radius:50%;background:var(--teal);display:block}
.foot-col{top:3559px;font-size:7px;line-height:14.5px;color:var(--muted)}
.foot-col h4{font-size:8.5px;font-weight:700;color:var(--navy);margin-bottom:4px}
.fine{font-size:6.5px;color:var(--muted)}
</style>
</head>
<body>

<section class="brand-board">
  <div class="abs wordmark">Corvanti, LLC</div>
  <div class="abs board-label" style="left:509px;top:102px">Fonts:</div>
  <div class="abs font-name" style="left:509px;top:142px">Halden Sans Pro</div>
  <div class="abs board-label" style="left:840px;top:102px">Colors:</div>
  <div class="abs swatch" style="left:843px;top:137px;background:#0e284b"></div>
  <div class="abs swatch" style="left:895px;top:137px;background:#1c3764"></div>
  <div class="abs swatch" style="left:945px;top:137px;background:#00b4cb"></div>
  <div class="abs swatch" style="left:997px;top:137px;background:#f4f5f6"></div>
  <div class="abs hex" style="left:833px;top:188px">#0e284b</div>
  <div class="abs hex" style="left:885px;top:188px">#1c3764</div>
  <div class="abs hex" style="left:935px;top:188px">#00b4cb</div>
  <div class="abs hex" style="left:987px;top:188px">#f4f5f6</div>
</section>

<main class="site">
  <header class="hero">
    <div class="abs hero-photo" role="img" aria-label="Smiling nurse in teal scrubs holding a tablet, with teal diagonal stripes behind her"></div>
    <nav class="abs nav">
      <div class="nav-brand">Corvanti, LLC</div>
      <div class="nav-links"><span>Features</span><span>About</span><span>Services</span><span>How it Works</span><span>Testimonials</span><span>FAQs</span></div>
      <div class="nav-cta">Sign Up For Free</div>
    </nav>
    <div class="abs eyebrow" style="left:74px;top:167px">Welcome to Corvanti LLC</div>
    <h1 class="abs hero-title">Medical Billing<br>Made Easy</h1>
    <p class="abs hero-sub">Delivering Comprehensive Revenue Cycle Management Solutions to Healthcare Providers and Billing Firms Nationwide.</p>
    <div class="abs btn-outline">See How it Works</div>
    <div class="abs stat-badge">
      <svg width="70" height="42" viewBox="0 0 70 42" style="margin-top:6px">
        <path d="M8 6 A27 27 0 0 0 62 6" fill="none" stroke="#e6eef4" stroke-width="8"/>
        <path d="M8 6 A27 27 0 0 0 35 33" fill="none" stroke="#00b4cb" stroke-width="8"/>
        <text x="35" y="14" text-anchor="middle" font-family="Mulish, sans-serif" font-size="9" font-weight="700" fill="#1c3764">50%</text>
      </svg>
      <p>11454 Successful<br>Claims Confirmed</p>
    </div>
  </header>

  <section class="perks">
    <div class="perk" style="left:74px"><svg width="24" height="24" viewBox="0 0 24 24" fill="none" stroke="#00b4cb" stroke-width="1.4"><path d="M12 2v20M8 6c4-2 8 0 8 3s-8 3-8 6 4 4 8 2"/></svg><span>HIPAA<br>Compliant</span></div>
    <div class="perk" style="left:246px"><svg width="28" height="24" viewBox="0 0 28 24" fill="none" stroke="#00b4cb" stroke-width="1.4"><rect x="2" y="4" width="24" height="17" rx="2"/><circle cx="9" cy="11" r="3"/><path d="M5 18c1-3 7-3 8 0M16 10h7M16 14h7"/></svg><span>Credentialing and<br>Credentialing<br>Maintenance</span></div>
    <div class="perk" style="left:455px"><svg width="24" height="26" viewBox="0 0 24 26" fill="none" stroke="#00b4cb" stroke-width="1.4"><rect x="3" y="2" width="18" height="22" rx="2"/><path d="M7 8h10M7 12h10M7 16h6"/></svg><span>Pay Only for<br>the Service</span></div>
    <div class="perk" style="left:633px"><svg width="26" height="26" viewBox="0 0 26 26" fill="none" stroke="#00b4cb" stroke-width="1.4"><circle cx="13" cy="13" r="11"/><path d="M13 6v14M9 10c0-2 8-2 8 1s-8 2-8 5 8 3 8 0"/></svg><span>Minimize<br>Cash Flow</span></div>
  </section>

  <div class="intro-mark"><span>Corvanti</span></div>
  <div class="intro-text">
    <div class="eyebrow" style="letter-spacing:2px">Introduction</div>
    <h2 class="section-title" style="margin:6px 0 16px">Who Are We?</h2>
    <p class="body-copy">We are a Northeast Arkansas medical billing and consulting company dedicated to providing efficient revenue cycle management and customer service with no interruption of cash flow to our clients.</p>
    <p class="body-copy" style="margin-top:10px">We handle maintaining the workflow of claim submissions to let provider's focus on patient care.</p>
  </div>

  <section class="services">
    <div class="abs eyebrow center" style="top:56px;letter-spacing:3px">Services</div>
    <h2 class="abs section-title center" style="top:68px">How We Help You</h2>
    <div class="card" style="left:74px"><div class="icon"><svg width="16" height="18" viewBox="0 0 16 18" fill="none" stroke="#1c3764" stroke-width="1.2"><rect x="2" y="1" width="12" height="16" rx="1"/><path d="M5 6h6M5 9h6M5 12h4"/></svg></div><h3>Patient Statements</h3><p>Simplify the patient billing experience, helping healthcare providers maintain transparency and efficiency in their financial transactions.</p></div>
    <div class="card" style="left:300px"><div class="icon"><svg width="18" height="16" viewBox="0 0 18 16" fill="none" stroke="#1c3764" stroke-width="1.2"><rect x="1" y="2" width="16" height="12" rx="1"/><path d="M1 6h16M4 10h5"/></svg></div><h3>Claims Submission</h3><p>Simplify the patient billing experience, helping healthcare providers maintain transparency and efficiency in their financial transactions.</p></div>
    <div class="card" style="left:525px"><div class="icon"><svg width="16" height="18" viewBox="0 0 16 18" fill="none" stroke="#1c3764" stroke-width="1.2"><rect x="2" y="1" width="12" height="16" rx="1"/><path d="M5 6l1.5 1.5L9 5M5 11l1.5 1.5L9 10"/></svg></div><h3>Eligibility &amp; Benefits</h3><p>Simplify the patient billing experience, helping healthcare providers maintain transparency and efficiency in their financial transactions.</p></div>
    <svg class="abs" style="left:378px;top:353px" width="36" height="10" viewBox="0 0 36 10" fill="none" stroke-width="1.3"><path d="M10 5H2M5 2L2 5l3 3" stroke="#b9c2cd"/><path d="M24 5h9M30 2l3 3-3 3" stroke="#00b4cb"/></svg>
  </section>

  <section class="proof">
    <p class="proof-text">Recommended by a <em>Growing</em><br><em>Network</em> of Content Enthusiasts</p>
    <div class="proof-stat" style="left:572px">7.4k<small>Happy Users</small></div>
    <div class="proof-stat" style="left:666px">95%<small>Positive Rating</small></div>
  </section>

  <div class="eyebrow center" style="top:1634px;letter-spacing:4px">How it works</div>
  <h2 class="section-title center" style="top:1650px;font-weight:500">Discover How Corvanti Works</h2>

  <h3 class="row-title" style="left:74px;top:1803px">All your accounts.<br>All in one place.</h3>
  <div style="left:74px;top:1880px;width:272px">
    <p class="body-copy">In addition to our expertise, we prioritize customer service. We understand that communication is key in the healthcare industry, and we make it a point to be responsive and accessible to address any questions or concerns you may have.</p>
    <p class="body-copy" style="margin-top:10px">We stay up-to-date with the latest industry regulations and best practices to ensure that you receive optimal reimbursement for the services you provide.</p>
  </div>
  <div class="photo" style="left:382px;top:1709px;width:336px;height:360px;background:linear-gradient(135deg,#dfe6ee 0%,#b7c6d6 50%,#5fb9c9 100%)" role="img" aria-label="Senior doctor in a white coat shaking hands with a smiling nurse"></div>

  <div class="photo" style="left:39px;top:2100px;width:340px;height:309px;background:linear-gradient(135deg,#cfd8e2 0%,#8ea5bd 50%,#3fb4c9 100%)" role="img" aria-label="Doctor and nurse reviewing records together on a tablet"></div>
  <h3 class="row-title" style="left:442px;top:2178px">Unlocking the Secrets to<br>Effortless Medical Billing</h3>
  <p class="body-copy" style="left:442px;top:2250px;width:268px">Maintaining our client base since our founding in 2015 has been possible due to our consistent delivery of exceptional services at affordable rates.</p>
  <div class="checks" style="left:442px;top:2311px">
    <span><i class="tick"></i>Text Filler Goes Here</span><span><i class="tick"></i>Text Filler Goes Here</span>
    <span><i class="tick"></i>Text Filler Goes Here</span><span><i class="tick"></i>Text Filler Goes Here</span>
  </div>

  <section class="testimonial">
    <svg class="abs" style="left:380px;top:58px" width="32" height="26" viewBox="0 0 32 26" fill="#00b4cb"><path d="M2 26V15C2 7 6 2 13 0l1 4c-4 2-6 5-6 9h6v13zM18 26V15c0-8 4-13 11-15l1 4c-4 2-6 5-6 9h6v13z"/></svg>
    <p class="abs center body-copy" style="top:104px;font-size:9px;line-height:14px;color:var(--ink)">“A wonderful serenity has taken possession of my entire soul,<br>like these sweet mornings of spring which I enjoy.”</p>
    <p class="abs center fine" style="top:154px">Lena Harwick</p>
  </section>

  <div class="contact-photo" role="img" aria-label="Healthcare worker in blue scrubs writing notes beside a calculator and medicine bottles"></div>
  <section class="contact">
    <div class="abs eyebrow" style="left:73px;top:58px;letter-spacing:2px">Request a free quote</div>
    <h2 class="abs section-title" style="left:73px;top:72px;color:#fff;font-size:21px;font-weight:500">Ready to Get Started?</h2>
    <div class="abs field-label" style="left:73px;top:120px">Full Name*</div>
    <div class="abs field-label" style="left:204px;top:120px">Phone Number*</div>
    <div class="abs field" style="left:73px;top:136px;width:118px;height:28px"></div>
    <div class="abs field" style="left:204px;top:136px;width:118px;height:28px"></div>
    <div class="abs field-label" style="left:73px;top:178px">Email Address*</div>
    <div class="abs field" style="left:73px;top:193px;width:249px;height:28px"></div>
    <div class="abs field-label" style="left:73px;top:236px">Inquiry*</div>
    <div class="abs field" style="left:73px;top:251px;width:249px;height:68px"></div>
    <div class="abs btn-solid" style="left:73px;top:337px;width:92px;height:28px">Submit Request</div>
  </section>

  <section class="faq">
    <div class="abs eyebrow center" style="top:62px;letter-spacing:2px">FAQs</div>
    <h2 class="abs section-title center" style="top:76px;font-weight:500">Frequently Asked Questions</h2>
    <div class="faq-list">
      <div class="faq-item"><span>What is Corvanti and what does it offer</span><b>+</b></div>
      <div class="faq-item"><span>What is Corvanti and what does it offer</span><b>+</b></div>
      <div class="faq-item"><span>What is Corvanti and what does it offer</span><b>+</b></div>
      <div class="faq-item"><span>What is Corvanti and what does it offer</span><b>+</b></div>
      <div class="faq-item" style="border:none"><span>What is Corvanti and what does it offer</span><b>+</b></div>
    </div>
  </section>

  <div class="footer-brand">Corvanti, LLC</div>
  <div class="socials"><i></i><i></i><i></i></div>
  <div class="foot-col" style="left:74px"><h4>Links</h4>About<br>Features<br>Testimonials<br>Faqs<br>Quote</div>
  <div class="foot-col" style="left:207px"><h4>Industries</h4>Text Filler<br>Text Filler<br>Text Filler</div>
  <div class="foot-col" style="left:342px"><h4>Services</h4>Text Filler<br>Text Filler<br>Text Filler<br>Text Filler</div>
  <div class="foot-col" style="left:466px"><h4>Headquarters</h4>12 Alder Lane, Suite 4<br>Northeast Arkansas</div>
  <div class="foot-col" style="left:656px"><h4>Contact Us</h4>info@corvanti.llc<br>+1 555 010 2040</div>
  <div class="fine" style="left:74px;top:3678px">©Copyright</div>
  <div class="fine" style="left:680px;top:3678px">Privacy Policy</div>
</main>

</body>
</html>
```